Upmarket Dessert Lounge needs a Business Card Design

We are an upmarket dessert lounge needing a business card to match our image.

We want something that is simple yet beautiful, feminine, classy, sophisticated and elegant. We want it to stand out and don't mind if it is bold.

The design should include our logo and colours of red or maroon with gold highlights. We don't mind if black is used.

Marlow & Quince

Target Market(s)

For those who like to indulge or treat themselves and give in to their temptations on good quality desserts.

Industry/Entity Type

Business

Requirements
Must have
• Must include our logo and our name

Marlow & Quince

M & Q

```html
<!DOCTYPE html>
<html lang="en">
<head>
<meta charset="utf-8">
<title>Marlow &amp; Quince — Business Card</title>
<link href="https://fonts.googleapis.com/css2?family=Cinzel:wght@500&family=Open+Sans:wght@400;600&family=Libre+Baskerville&display=swap" rel="stylesheet">
<style>
  :root {
    --bg: #e9e6e2;
    --maroon: #8e1b1b;
    --maroon-deep: #5e0f10;
    --maroon-light: #a82a25;
    --gold: #e2b07a;
    --gold-soft: #c99663;
    --cream: #f6c592;
    --band: #2a1210;
    --ink-dark: #5a1a14;
  }
  * { box-sizing: border-box; margin: 0; padding: 0; }
  html, body { width: 1200px; height: 951px; overflow: hidden; background: var(--bg); }
  .canvas { position: relative; width: 1200px; height: 951px; }

  .card {
    position: absolute;
    width: 620px; height: 354px;
    border-radius: 22px;
    overflow: hidden;
    box-shadow: 0 10px 26px rgba(0,0,0,.22);
  }

  /* Front */
  .card-front {
    left: 70px; top: 90px;
    background: radial-gradient(ellipse at 45% 40%, var(--maroon-light) 0%, var(--maroon) 50%, var(--maroon-deep) 100%);
  }
  .flourish {
    position: absolute;
    background: linear-gradient(200deg, rgba(226,176,122,.55), rgba(226,176,122,.08) 70%, transparent);
    border-bottom-left-radius: 100% 90%;
  }
  .card-front .flourish { top: 0; right: 0; width: 250px; height: 110px; }
  .front-name {
    position: absolute; left: 0; right: 0; top: 120px;
    text-align: center;
    font-family: "Cinzel", serif; font-weight: 500;
    font-size: 44px; letter-spacing: 2px;
    color: var(--gold);
  }
  .front-web {
    position: absolute; left: 0; right: 0; top: 268px;
    text-align: center;
    font-family: "Libre Baskerville", serif;
    font-size: 17px; letter-spacing: 1px;
    color: var(--gold);
  }

  /* Back */
  .card-back {
    left: 510px; top: 500px;
    background: radial-gradient(ellipse at 70% 55%, var(--maroon-light) 0%, var(--maroon) 55%, var(--maroon-deep) 100%);
  }
  .back-shape { position: absolute; inset: 0; }
  .card-back .flourish { top: 0; right: 0; width: 230px; height: 110px; }
  .back-title {
    position: absolute; left: 30px; top: 32px;
    font-family: "Open Sans", sans-serif; font-weight: 600;
    font-size: 22px; color: var(--ink-dark);
  }
  .back-title .amp { color: #fff; }
  .monogram {
    position: absolute; left: 38px; top: 150px;
    width: 176px; text-align: center;
    font-family: "Cinzel", serif; font-weight: 500;
    font-size: 50px; color: var(--maroon);
  }
  .contact {
    position: absolute; left: 350px; top: 138px;
    list-style: none;
    font-family: "Open Sans", sans-serif; font-size: 19px;
    line-height: 24px; color: #fff;
  }
  .contact li { display: flex; align-items: flex-start; gap: 10px; }
  .contact li + li { margin-top: 0; }
  .contact .gap { margin-top: 28px; }
  .contact svg { flex: none; width: 16px; height: 16px; margin-top: 4px; fill: var(--gold); }
</style>
</head>
<body>
<main class="canvas">

  <section class="card card-front" aria-label="Card front">
    <div class="flourish" role="img" aria-label="Gold scrolling flourish ornament"></div>
    <h1 class="front-name">Marlow &amp; Quince</h1>
    <p class="front-web">www.marlowquince.com</p>
  </section>

  <section class="card card-back" aria-label="Card back">
    <svg class="back-shape" viewBox="0 0 620 354" width="620" height="354" aria-hidden="true">
      <path d="M0 0 H262 C222 90 300 210 236 354 H0 Z" fill="var(--band)"/>
      <path d="M0 0 H244 C206 90 282 210 216 354 H0 Z" fill="var(--cream)"/>
    </svg>
    <div class="flourish" role="img" aria-label="Gold scrolling flourish ornament"></div>
    <p class="back-title">Marlow <span class="amp">&amp;</span> Quince</p>
    <p class="monogram">M &amp; Q</p>
    <ul class="contact">
      <li>
        <svg viewBox="0 0 16 16"><path d="M8 1 L15 8 H13 V15 H9.5 V10.5 H6.5 V15 H3 V8 H1 Z"/></svg>
        <span>1840 Velvet Row<br>Suite 204-118<br>Harlow, TX 75510</span>
      </li>
      <li class="gap">
        <svg viewBox="0 0 16 16"><path d="M4 1 L6.5 4.5 L5 6.5 C6 8.5 7.5 10 9.5 11 L11.5 9.5 L15 12 L13 15 C7 14 2 9 1 3 Z"/></svg>
        <span>555-014-2290</span>
      </li>
      <li>
        <svg viewBox="0 0 16 16"><rect x="4" y="1" width="8" height="14" rx="1.5"/></svg>
        <span>555-014-2291</span>
      </li>
      <li>
        <svg viewBox="0 0 16 16"><rect x="1" y="3.5" width="14" height="9" rx="1"/></svg>
        <span>hello@marlowquince.com</span>
      </li>
      <li>
        <svg viewBox="0 0 16 16"><circle cx="8" cy="8" r="7"/></svg>
        <span>www.marlowquince.com</span>
      </li>
    </ul>
  </section>

</main>
</body>
</html>
```